A business selling natural soaps online and in farmers markets. I want it to reflect local commerce and natural lifestyle. My colors are olive green and saddle brown. I want the dimensions to be 2.25 x 3.25" with matte finish.

The name of my company is Fernwick Soapery, LLC

Business

```html
<!DOCTYPE html>
<html lang="en">
<head>
<meta charset="utf-8">
<title>Fernwick Soapery – Business Card</title>
<link rel="stylesheet" href="https://fonts.googleapis.com/css2?family=Courier+Prime:wght@700&family=Open+Sans:wght@400&display=swap">
<style>
  :root {
    --saddle: #98622f;
    --saddle-dark: #83521f;
    --olive: #8b8b4e;
    --olive-light: #94945a;
    --ink: #3f2914;
  }
  * { margin: 0; padding: 0; box-sizing: border-box; }
  html, body {
    width: 1200px;
    height: 831px;
    overflow: hidden;
    background: var(--saddle);
  }
  .card {
    position: relative;
    width: 1200px;
    height: 831px;
    background: linear-gradient(90deg, var(--saddle-dark), var(--saddle) 50%, var(--saddle-dark));
    color: var(--ink);
  }
  .card__panel {
    position: absolute;
    left: 0;
    top: 80px;
    width: 1200px;
    height: 662px;
    background: linear-gradient(180deg, var(--olive-light), var(--olive) 55%, #86864a);
  }
  .card__brand {
    position: absolute;
    top: 166px;
    left: 0;
    width: 100%;
    text-align: center;
    font-family: "Courier Prime", "Courier New", monospace;
    font-weight: 700;
    font-size: 66px;
    line-height: 1;
    letter-spacing: 1px;
  }
  .card__rule {
    position: absolute;
    top: 264px;
    left: 101px;
    width: 1030px;
    height: 4px;
    background: var(--ink);
  }
  .card__name {
    position: absolute;
    top: 349px;
    left: 0;
    width: 100%;
    text-align: center;
    font-family: "Courier Prime", "Courier New", monospace;
    font-weight: 700;
    font-size: 50px;
    line-height: 1;
  }
  .card__role {
    position: absolute;
    top: 424px;
    left: 0;
    width: 100%;
    text-align: center;
    font-family: "Courier Prime", "Courier New", monospace;
    font-weight: 700;
    font-size: 29px;
    line-height: 1;
  }
  .card__contact {
    position: absolute;
    top: 654px;
    left: -16px;
    width: 100%;
    text-align: center;
    font-family: "Open Sans", Arial, sans-serif;
    font-weight: 400;
    font-size: 36px;
    line-height: 1;
  }
  .card__dot { padding: 0 8px; }
</style>
</head>
<body>
  <div class="card">
    <div class="card__panel" role="img" aria-label="Olive green brushed paint texture"></div>
    <h1 class="card__brand">Fernwick Soapery</h1>
    <div class="card__rule"></div>
    <p class="card__name">Clara Hadley</p>
    <p class="card__role">Owner</p>
    <p class="card__contact">fernwicksoap.com<span class="card__dot">•</span>info@fernwicksoap.com</p>
  </div>
</body>
</html>
```